Adelaide based cleaning and remediation business needs a website design

We are launching a new company with no clients as yet so we don't have the benefit of Veltrano Ratings to build confidence. We can use our  past work history with other employers in the industry to give some credibility. Happy to use any colour scheme as long as it look interesting when people click on the site it gets there attention. enquiry . I have supplied a mock up the important information and various photos as they tell a lot of the story.

```html
<!DOCTYPE html>
<html lang="en">
<head>
<meta charset="utf-8">
<title>Marrow Services Pty Ltd</title>
<link href="https://fonts.googleapis.com/css2?family=Bowlby+One&family=Poppins:wght@400;500;600&display=swap" rel="stylesheet">
<style>
:root{
  --ink:#1d1d1f;
  --muted:#9a9a9a;
  --accent:#e6413b;
  --purple:#9a4c8e;
  --purple-dark:#6f3a6e;
  --sage:#eef1ea;
  --pink:#f6dfe1;
  --btn-a:#e0646f;
  --btn-b:#a06aa3;
  --white:#ffffff;
  --hero-dark:#2b2118;
}
*{box-sizing:border-box;margin:0;padding:0}
html,body{width:1200px;height:4850px;overflow:hidden}
body{position:relative;background:var(--white);font-family:"Poppins",sans-serif;color:var(--ink)}
.abs{position:absolute}
.heading{font-family:"Bowlby One",sans-serif;font-weight:400;text-transform:uppercase;color:var(--ink);line-height:1.05}
.body-text{font-size:14px;line-height:1.45;color:#333}
.btn-grad{position:absolute;height:42px;padding:0 36px;border-radius:21px;background:linear-gradient(90deg,var(--btn-a),var(--btn-b));color:#fff;font-size:12px;font-weight:600;display:flex;align-items:center;text-transform:uppercase}
.photo{position:absolute;border-radius:50%;border:2px dashed rgba(230,65,59,.55);padding:10px}
.photo .fill{width:100%;height:100%;border-radius:50%}
.ring{position:absolute;border-radius:50%}

.hero{position:absolute;left:0;top:0;width:1200px;height:760px;overflow:hidden}
.hero-photo{position:absolute;inset:0;background:radial-gradient(ellipse at 70% 35%,#8a6a45 0%,#4e3a27 35%,var(--hero-dark) 75%)}
.topbar{position:absolute;left:350px;top:0;width:850px;height:38px;background:var(--purple);border-bottom-left-radius:30px;display:flex;align-items:center;gap:44px;padding-left:90px;color:#fff;font-size:12px;font-weight:500}
.topbar span{display:flex;align-items:center;gap:8px}
.brand{position:absolute;left:84px;top:30px;display:flex;align-items:center;gap:8px;color:#fff;font-size:15px;font-weight:600}
.brand i{width:14px;height:14px;background:#fff;display:block}
.nav{position:absolute;left:254px;top:66px;display:flex;gap:42px;color:#fff;font-size:13px;font-weight:600}
.quote-top{position:absolute;left:952px;top:52px;width:158px;height:44px;border-radius:22px;background:#fff;font-size:13px;font-weight:600;display:flex;align-items:center;justify-content:center}
.hero-title1{position:absolute;left:86px;top:220px;font-size:54px;color:#fff}
.hero-title2{position:absolute;left:86px;top:272px;font-size:122px;color:#fff;line-height:1}
.hero-lede{position:absolute;left:88px;top:400px;width:480px;font-size:14px;line-height:1.45;color:#fff}
.hero-btn{position:absolute;top:462px;height:44px;border-radius:22px;font-size:13px;font-weight:600;display:flex;align-items:center;justify-content:center}
.hero-btn.solid{left:88px;width:202px;background:#fff}
.hero-btn.ghost{left:300px;width:152px;border:1.5px solid #fff;color:#fff}

.about-h{left:618px;top:862px;font-size:40px}
.about-p{left:618px;top:914px;width:462px}

.band{position:absolute;left:0;width:1200px}

.pigeon-h{left:119px;top:1430px;font-size:40px}
.pigeon-p{left:119px;top:1482px;width:485px}

.fire-h{left:0;width:1200px;top:1920px;font-size:40px;text-align:center}
.fire-p{left:340px;width:520px;top:1983px;text-align:center}

.squalor-h{left:577px;top:2556px;font-size:40px}
.squalor-p{left:577px;top:2662px;width:440px}

.col-h{top:3080px;font-size:40px}
.col-p{top:3136px;width:450px}
.divider-v{position:absolute;left:599px;top:3090px;width:1px;height:175px;background:#ddd}
.badge{position:absolute;left:669px;top:3210px;display:flex;align-items:center;gap:10px}
.badge i{display:block;width:54px;height:54px;border-radius:50%;background:radial-gradient(circle,#8ac43f,#2b6aa8)}
.badge b{display:block;width:90px;height:16px;background:#dfe7ef;border-radius:3px}
.divider-h{position:absolute;left:0;top:3325px;width:1200px;height:1px;background:#e6e6e6}

.best-h{left:0;width:1200px;top:3380px;font-size:40px;text-align:center}
.card{position:absolute;top:3500px;width:438px;height:343px;background:#fff;border-radius:12px;box-shadow:0 6px 28px rgba(0,0,0,.08);padding:36px}
.card .q{font-family:"Bowlby One",sans-serif;color:var(--accent);font-size:60px;line-height:.8;height:48px}
.card p{font-size:14px;line-height:1.75;color:#333;margin-top:14px;width:340px}
.card .who{position:absolute;left:36px;bottom:58px;font-family:"Bowlby One",sans-serif;font-size:12px;text-transform:uppercase}
.card .role{position:absolute;left:36px;bottom:36px;font-size:13px;color:var(--muted)}
.card .rate{position:absolute;right:36px;bottom:58px;display:flex;align-items:center;gap:6px;font-size:16px}
.dots{position:absolute;left:585px;top:3880px;display:flex;gap:6px}
.dots i{width:9px;height:9px;border-radius:50%;background:#e9a23b;display:block}
.dots i+i{background:#f1c98a}

.qq-h{left:109px;top:4104px;font-size:40px}
.qq-item{position:absolute;left:114px;display:flex;align-items:center;gap:22px}
.qq-icon{width:70px;height:70px;border-radius:50%;background:var(--accent);box-shadow:0 0 0 7px rgba(255,255,255,.8);display:flex;align-items:center;justify-content:center}
.qq-item b{display:block;font-family:"Bowlby One",sans-serif;font-weight:400;font-size:15px;text-transform:uppercase}
.qq-item span{font-size:14px}

.form{position:absolute;left:640px;top:4013px;width:450px;height:580px;background:#fff;border-top:5px solid var(--accent);border-radius:10px;box-shadow:0 10px 30px rgba(0,0,0,.08);padding:38px 28px}
.form h2{font-size:40px}
.field{position:absolute;left:28px;width:394px;border-bottom:1px solid #ddd;height:58px}
.field label{font-size:14px;display:block}
.field span{font-size:14px;color:#aaa}
.field svg{position:absolute;right:8px;top:24px}
.choose{position:absolute;left:28px;top:507px;width:140px;height:42px;border:1.5px solid #222;border-radius:21px;font-size:13px;font-weight:600;display:flex;align-items:center;justify-content:center}
.drop{position:absolute;left:180px;top:520px;font-size:13px;font-weight:600}
.send{position:absolute;left:328px;top:507px;width:94px;height:42px;border-radius:21px;background:linear-gradient(90deg,var(--btn-a),var(--btn-b));color:#fff;font-size:13px;font-weight:600;display:flex;align-items:center;justify-content:center}

.f-brand{position:absolute;left:150px;top:4630px;color:#fff;font-size:22px;font-weight:600;display:flex;align-items:center;gap:10px}
.f-brand i{width:18px;height:18px;background:#fff;display:block}
.social{position:absolute;top:4750px;height:28px;border-radius:14px;padding:0 10px;font-size:11px;font-weight:600;display:flex;align-items:center}
.f-col{position:absolute;top:4638px;color:#fff}
.f-col h4{font-family:"Bowlby One",sans-serif;font-weight:400;font-size:13px;text-transform:uppercase;border-left:2px solid #fff;padding-left:8px;line-height:1.1}
.f-col p,.f-col li{font-size:11px;line-height:1.6;list-style:none;padding-left:10px}
.f-col ul{margin-top:10px}
.email-in{position:absolute;left:840px;top:4738px;width:214px;height:36px;background:#fff;border-radius:18px;font-size:10px;color:#aaa;display:flex;align-items:center;padding-left:20px}
.email-go{position:absolute;left:1012px;top:4738px;width:42px;height:36px;border-radius:18px;background:#f3d23a;display:flex;align-items:center;justify-content:center}
.copy{position:absolute;left:96px;top:4820px;color:#fff;font-size:9px}
.pay{position:absolute;top:4812px;height:22px;width:42px;border-radius:3px;background:#fff;font-size:8px;font-weight:600;display:flex;align-items:center;justify-content:center;color:var(--ink)}
</style>
</head>
<body>

<header class="hero">
  <div class="hero-photo" role="img" aria-label="Photo of a cluttered, dark storage room filled with junk and debris"></div>
  <svg class="abs" style="left:0;top:0" width="1200" height="760" viewBox="0 0 1200 760">
    <path d="M0 600 C120 700 260 700 420 690 C640 676 900 600 1200 560 L1200 760 L0 760 Z" fill="#fff"/>
    <path d="M190 715 C330 760 520 740 720 690 C880 650 1040 615 1200 600 C1040 630 880 670 720 712 C520 762 320 770 190 715 Z" fill="#e6413b"/>
  </svg>
  <div class="topbar">
    <span><svg width="12" height="12" viewBox="0 0 24 24"><path fill="#fff" d="M6.6 10.8a15 15 0 006.6 6.6l2.2-2.2c.3-.3.7-.4 1-.2 1.1.4 2.3.6 3.6.6.6 0 1 .4 1 1V20c0 .6-.4 1-1 1A17 17 0 013 4c0-.6.4-1 1-1h3.5c.6 0 1 .4 1 1 0 1.3.2 2.5.6 3.6.1.3 0 .7-.2 1z"/></svg>0491570156</span>
    <span><svg width="13" height="11" viewBox="0 0 24 20"><rect x="1" y="1" width="22" height="18" rx="2" fill="#fff"/><path d="M2 3l10 8 10-8" stroke="#9a4c8e" stroke-width="2" fill="none"/></svg>admin@marrowservices.com</span>
    <span><svg width="10" height="13" viewBox="0 0 20 26"><path fill="#fff" d="M10 0a9 9 0 00-9 9c0 7 9 17 9 17s9-10 9-17a9 9 0 00-9-9zm0 12a3 3 0 110-6 3 3 0 010 6z"/></svg>12 Tarlee Street Norwood SA 5067</span>
  </div>
  <div class="brand"><i></i>Marrow</div>
  <nav class="nav"><span>HOME</span><span>ABOUT US</span><span>SERVICES</span><span>CONTACT US</span></nav>
  <div class="quote-top">GET A QUOTE</div>
  <h1 class="heading hero-title1">Marrow Services</h1>
  <div class="heading hero-title2">Pty Ltd</div>
  <p class="hero-lede">Lorem Ipsum is simply dummy text of the printing and typesetting industry. Lorem Ipsum has been the industry's standard dummy</p>
  <div class="hero-btn solid">DIRTY JOB CLEANERS</div>
  <div class="hero-btn ghost">GET A QUOTE</div>
</header>

<div class="photo" style="left:120px;top:808px;width:400px;height:400px"><div class="fill" role="img" aria-label="Photo of a worker in a blue protective suit and respirator carrying a green basket through debris" style="background:radial-gradient(circle at 55% 45%,#7ea3c9,#4b4a46 60%,#2c2a27)"></div></div>
<h2 class="heading abs about-h">About Us</h2>
<p class="abs body-text about-p">Adelaide-based Marrow Services is a family-run organisation.We have been in operation for more than two decades.We've gained some knowledge about cleaning and squalor removal services throughout the years. As a small South Australian company, we base everything on responsibility honesty and fairness .We are aware of the confidence you put in us when you seek our help</p>
<div class="btn-grad" style="left:618px;top:1078px">Read More</div>
<div class="ring" style="left:1122px;top:1075px;width:80px;height:80px;background:#f7c9cc"></div>
<div class="ring" style="left:1062px;top:1128px;width:112px;height:112px;border:1.5px solid #f0a5a8"></div>

<svg class="band" style="top:1200px" width="1200" height="680" viewBox="0 0 1200 680">
  <path d="M0 90 C220 10 420 40 620 70 C820 100 1000 20 1200 40 L1200 560 C1000 540 860 620 620 640 C380 660 160 540 0 580 Z" fill="#eef1ea"/>
</svg>
<h2 class="heading abs pigeon-h">Pigeon Waste</h2>
<p class="abs body-text pigeon-p">Can cause damage to buildings and spread disease, mites and bacteria, triggering alarms and damaging the reputation of businesses. 1. The pigeon faeces is carefully removed by our trained operatives, who also dispose of it in an environmentally friendly way. 2. Next, in order to remove stains and ensure safety, we use eco-friendly chemicals to clean and disinfect the impacted areas. 3.We advise adding anti-nesting spikes as an option.</p>
<div class="btn-grad" style="left:119px;top:1643px">Leaen More</div>
<div class="photo" style="left:701px;top:1332px;width:404px;height:404px"><div class="fill" role="img" aria-label="Photo of a worker in white protective gear cleaning a roof gutter covered in pigeon droppings" style="background:radial-gradient(circle at 45% 40%,#d9d4c8,#7a6a58 55%,#2f2a25)"></div></div>

<h2 class="heading abs fire-h">Fire Damage Clean Outs</h2>
<p class="abs body-text fire-p">Removal of debris; On site cleaning of contents; Cleaning of carpets and upholstered items; Catalogue all contents for packing and storage Pressure cleaning of contaminated surfaces;</p>
<div class="photo" style="left:214px;top:2068px;width:234px;height:234px;padding:7px"><div class="fill" role="img" aria-label="Photo of pigeons perched on a ledge above a wall stained with droppings" style="background:linear-gradient(180deg,#eae8e3,#bcb3a2 60%,#8c7c66)"></div></div>
<div class="photo" style="left:482px;top:2068px;width:234px;height:234px;padding:7px"><div class="fill" role="img" aria-label="Photo of a dusty floor covered in bird waste beside a stairway" style="background:radial-gradient(circle,#b8b2a6,#6e665c 70%,#3b362f)"></div></div>
<div class="photo" style="left:752px;top:2068px;width:234px;height:234px;padding:7px"><div class="fill" role="img" aria-label="Photo of a worker in a white suit clearing droppings in a roof space" style="background:radial-gradient(circle at 55% 50%,#d6d6d2,#6d6455 60%,#2e2a24)"></div></div>
<div class="ring" style="left:38px;top:2268px;width:112px;height:112px;border:1.5px solid #f0a5a8"></div>
<div class="ring" style="left:6px;top:2350px;width:80px;height:80px;background:#f7c9cc"></div>

<svg class="band" style="top:2370px" width="1200" height="620" viewBox="0 0 1200 620">
  <defs>
    <linearGradient id="sq" x1="0" y1="0" x2="1" y2="0.4">
      <stop offset="0" stop-color="#ece9dc"/>
      <stop offset=".45" stop-color="#f4d7d9"/>
      <stop offset=".75" stop-color="#e9d6de"/>
      <stop offset="1" stop-color="#eef1ea"/>
    </linearGradient>
  </defs>
  <path d="M0 60 C200 20 320 80 520 70 C760 56 900 -20 1200 30 L1200 520 C1000 470 880 520 700 560 C420 620 200 540 0 580 Z" fill="url(#sq)"/>
</svg>
<div class="photo" style="left:88px;top:2541px;width:400px;height:400px"><div class="fill" role="img" aria-label="Photo of a fire-damaged kitchen with a soot-blackened stove and walls" style="background:radial-gradient(circle at 40% 60%,#c9c3b8,#5c534a 50%,#1f1b18)"></div></div>
<h2 class="heading abs squalor-h">Squlaor Estate<br>Clean Ups</h2>
<p class="abs body-text squalor-p">Marrow Services is a hoarding clean up firm that approaches clutter removal personally. We always operate with compassion, prioritising the individuals involved over the cleaning procedure, and we understand the psychology of a person's hoarding attitude. We provide the following services Clutter Removal Search And Recovery Of Items: paperwork, collectibles, valuables, etc. Packing And Storing Deep Cleaning Odor Removal</p>
<div class="btn-grad" style="left:577px;top:2835px">Leaen More</div>

<h2 class="heading abs col-h" style="left:88px">Pricing</h2>
<p class="abs body-text col-p" style="left:88px">Prices provided in terms of the number of hours and service required or as a fixed quotation according to the quantity of clutter, pigeon faeces, and mould disposal expenses; however, hoarding cleaning can be different as this may require sorting and can require more organisation</p>
<div class="divider-v"></div>
<h2 class="heading abs col-h" style="left:669px">Qualifications</h2>
<p class="abs body-text col-p" style="left:669px">Mould Remediation CRSB Standard S520 CRSB Standard Trauma &amp; Crime Scene Cleans White Card Working at Heights National Police Cleared Working with vunerable people (DHS)</p>
<div class="badge"><i></i><b></b></div>
<div class="divider-h"></div>

<h2 class="heading abs best-h">Only the best service for<br>our customers</h2>
<div class="card" style="left:141px">
  <div class="q">&ldquo;</div>
  <p>Engaged Marrow Services to clean bird poo from our commercial building facade . Job was so well done it exceeded our expectations.</p>
  <div class="who">Tom Ravelli.</div>
  <div class="role">Halvern Building Maintenance</div>
  <div class="rate"><svg width="18" height="18" viewBox="0 0 24 24"><path fill="#f1a62c" d="M12 2l3 7 7 .6-5.4 4.6 1.7 7.3L12 17.8 5.7 21.5l1.7-7.3L2 9.6 9 9z"/></svg>5.7</div>
</div>
<div class="card" style="left:621px">
  <div class="q">&ldquo;</div>
  <p>Declan and his team arrived the next morning to clean up a rental property my husband and I own which and had been trashed by the tenants. He was the only contractor to return my call. They did an amazing job and also deodorised the house for no extra charge.</p>
  <div class="who">Nadia Pereval.</div>
  <div class="role">Satisfied customer</div>
  <div class="rate"><svg width="18" height="18" viewBox="0 0 24 24"><path fill="#f1a62c" d="M12 2l3 7 7 .6-5.4 4.6 1.7 7.3L12 17.8 5.7 21.5l1.7-7.3L2 9.6 9 9z"/></svg>5.7</div>
</div>
<div class="dots"><i></i><i></i></div>
<div class="ring" style="left:1098px;top:3880px;width:112px;height:112px;border:1.5px solid #f0a5a8"></div>
<div class="ring" style="left:1140px;top:3958px;width:80px;height:80px;background:#f7c9cc"></div>

<svg class="band" style="top:3990px" width="1200" height="860" viewBox="0 0 1200 860">
  <defs>
    <linearGradient id="ct" x1="0" y1="0" x2="1" y2="0">
      <stop offset="0" stop-color="#eef1ea"/>
      <stop offset=".6" stop-color="#f3e4e4"/>
      <stop offset="1" stop-color="#eef1ea"/>
    </linearGradient>
    <radialGradient id="ft" cx=".5" cy=".5" r=".8">
      <stop offset="0" stop-color="#8f4f86"/>
      <stop offset=".5" stop-color="#9a4c8e"/>
      <stop offset="1" stop-color="#5e2e5c"/>
    </radialGradient>
  </defs>
  <path d="M0 60 C300 0 560 80 820 50 C980 30 1100 10 1200 20 L1200 860 L0 860 Z" fill="url(#ct)"/>
  <path d="M0 460 C240 380 460 470 700 470 C940 470 1080 380 1200 400 L1200 860 L0 860 Z" fill="url(#ft)"/>
</svg>

<h2 class="heading abs qq-h">Get a quick quote</h2>
<div class="qq-item" style="top:4172px">
  <div class="qq-icon"><svg width="18" height="24" viewBox="0 0 20 26"><path fill="#fff" d="M10 0a9 9 0 00-9 9c0 7 9 17 9 17s9-10 9-17a9 9 0 00-9-9zm0 12a3 3 0 110-6 3 3 0 010 6z"/></svg></div>
  <div><b>Location</b><span>12 Tarlee Street Norwood SA 5067</span></div>
</div>
<div class="qq-item" style="top:4260px">
  <div class="qq-icon"><svg width="22" height="18" viewBox="0 0 24 20"><rect x="1" y="1" width="22" height="18" rx="2" fill="#fff"/><path d="M2 3l10 8 10-8" stroke="#e6413b" stroke-width="2" fill="none"/></svg></div>
  <div><b>E-mail</b><span>admin@marrowservices.com</span></div>
</div>
<div class="qq-item" style="top:4348px">
  <div class="qq-icon"><svg width="20" height="20" viewBox="0 0 24 24"><path fill="#fff" d="M6.6 10.8a15 15 0 006.6 6.6l2.2-2.2c.3-.3.7-.4 1-.2 1.1.4 2.3.6 3.6.6.6 0 1 .4 1 1V20c0 .6-.4 1-1 1A17 17 0 013 4c0-.6.4-1 1-1h3.5c.6 0 1 .4 1 1 0 1.3.2 2.5.6 3.6.1.3 0 .7-.2 1z"/></svg></div>
  <div><b>Phone</b><span>0491 570 156</span></div>
</div>

<form class="form">
  <h2 class="heading">Contact Us</h2>
  <div class="field" style="top:150px"><label>Name</label><span>Jonathan Doe</span><svg width="12" height="12" viewBox="0 0 24 24"><circle cx="12" cy="7" r="5" fill="#e6413b"/><path d="M3 23c0-6 4-9 9-9s9 3 9 9z" fill="#e6413b"/></svg></div>
  <div class="field" style="top:228px"><label>E-Mail</label><span>admin@marrowservices.com</span><svg width="12" height="10" viewBox="0 0 24 20"><rect x="1" y="1" width="22" height="18" rx="2" fill="#e6413b"/><path d="M2 3l10 8 10-8" stroke="#fff" stroke-width="2" fill="none"/></svg></div>
  <div class="field" style="top:302px"><label>phone</label><span>0491 570 156</span><svg width="12" height="12" viewBox="0 0 24 24"><path fill="#e6413b" d="M6.6 10.8a15 15 0 006.6 6.6l2.2-2.2c.3-.3.7-.4 1-.2 1.1.4 2.3.6 3.6.6.6 0 1 .4 1 1V20c0 .6-.4 1-1 1A17 17 0 013 4c0-.6.4-1 1-1h3.5c.6 0 1 .4 1 1 0 1.3.2 2.5.6 3.6.1.3 0 .7-.2 1z"/></svg></div>
  <div class="field" style="top:376px;height:80px"><label>Message</label><span>Lorem Ipsum is simply</span><svg width="12" height="12" viewBox="0 0 24 24"><path fill="#e6413b" d="M2 3h20v14H8l-6 5z"/></svg></div>
  <div class="choose">CHOOSE FILES</div>
  <div class="drop">or Drop Files Here</div>
  <div class="send">SEND</div>
</form>

<footer>
  <div class="f-brand"><i></i>Marrow</div>
  <div class="social" style="left:150px;background:#f3d23a">Linkra</div>
  <div class="social" style="left:222px;background:rgba(255,255,255,.3);color:#fff">Snapt</div>
  <div class="f-col" style="left:401px"><h4>Quick Links</h4><ul><li>Home</li><li>About us</li><li>Services</li><li>Contact Us</li></ul></div>
  <div class="f-col" style="left:608px"><h4>Business Hours</h4><ul><li>Monday to Saturday</li><li>8:00 am to 4:00 pm</li></ul></div>
  <div class="f-col" style="left:840px;width:220px"><h4>Newsletter Sign-Up</h4><ul><li>Sign up for the latest trends, offers, and exclusive deals from The Sample Sales Team</li></ul></div>
  <div class="email-in">Enter Email...</div>
  <div class="email-go"><svg width="16" height="12" viewBox="0 0 16 12"><path d="M1 6h13M9 1l5 5-5 5" stroke="#222" stroke-width="1.6" fill="none"/></svg></div>
  <div class="copy">Copyrights 2025,All Rights Reserved</div>
  <div class="pay" style="left:862px">Payvo</div>
  <div class="pay" style="left:912px">Tapli</div>
  <div class="pay" style="left:962px">Cardex</div>
  <div class="pay" style="left:1012px">Mondo</div>
  <div class="pay" style="left:1062px">Verra</div>
</footer>

</body>
</html>
```